Real Estate Business Cards

Looking for a clean, sharp and professional look for our Real Estate investment Fund that invests in Multi Family Apartment buildings.

Target Market(s)

Real Estate Fund

Industry/Entity Type

Real Estate

Contact Information for Business Card

Company Description: Real Estate Investment Fund
Company Name: RKW Holdings
Name: Marcus Olvane
Cell: (917) 482-0657
Email: marcus@rkwholdings-example.com
Website: www.rkwholdings-example.com
Address: 418, 9th Street, Brooklyn NY 11218

Colors

Designer to choose colors to be used in the design.

Requirements
Nice to have
• Colors to match logo

```html
<!DOCTYPE html>
<html lang="en">
<head>
<meta charset="utf-8">
<title>RKW Holdings – Business Cards</title>
<link rel="stylesheet" href="https://fonts.googleapis.com/css2?family=Cinzel:wght@400;500&family=Montserrat:wght@400;500&display=swap">
<style>
  :root {
    --backdrop: #3b312c;
    --card: #1c1c1d;
    --card-edge: #262627;
    --brand-blue: #1e7ab8;
    --text-light: #f2f2f2;
    --text-muted: #d8d8d8;
  }
  * { box-sizing: border-box; margin: 0; padding: 0; }
  html, body { width: 1200px; height: 716px; overflow: hidden; }
  body {
    background: var(--backdrop);
    position: relative;
    font-family: "Montserrat", sans-serif;
  }
  .card {
    position: absolute;
    top: 209px;
    width: 520px;
    height: 298px;
    background: linear-gradient(160deg, var(--card-edge), var(--card) 60%);
    border-radius: 6px;
    overflow: hidden;
  }
  .card-front { left: 50px; }
  .card-back { left: 630px; }

  /* Front */
  .front-lockup {
    position: absolute;
    inset: 0;
    display: flex;
    flex-direction: column;
    align-items: center;
    justify-content: center;
    gap: 18px;
  }
  .brand-square {
    width: 46px;
    height: 46px;
    background: var(--brand-blue);
    border-radius: 4px;
  }
  .brand-name {
    font-family: "Cinzel", serif;
    font-weight: 400;
    font-size: 30px;
    letter-spacing: 1px;
    color: var(--text-light);
  }

  /* Back */
  .back-brand {
    position: absolute;
    left: 34px;
    top: 30px;
    font-family: "Cinzel", serif;
    font-weight: 400;
    font-size: 20px;
    color: var(--brand-blue);
  }
  .contact-block {
    position: absolute;
    left: 34px;
    top: 78px;
    color: var(--text-light);
  }
  .person-name {
    font-family: "Cinzel", serif;
    font-weight: 500;
    font-size: 26px;
    color: var(--brand-blue);
    line-height: 1;
  }
  .person-title {
    font-size: 11px;
    margin-top: 4px;
    color: var(--text-muted);
  }
  .title-rule {
    width: 14px;
    height: 1px;
    background: var(--brand-blue);
    margin: 8px 0 10px;
  }
  .address { font-size: 11px; line-height: 1.45; }
  .contact-list { list-style: none; margin-top: 12px; font-size: 11px; line-height: 1.7; }
  .contact-list li { display: flex; align-items: center; gap: 7px; }
  .contact-list svg { width: 9px; height: 9px; fill: none; stroke: var(--brand-blue); stroke-width: 1.4; }
  .web-accent { color: var(--brand-blue); }
  .back-square {
    position: absolute;
    right: 34px;
    bottom: 34px;
    width: 150px;
    height: 150px;
    background: var(--brand-blue);
    border-radius: 10px;
  }
</style>
</head>
<body>
  <section class="card card-front">
    <div class="front-lockup">
      <div class="brand-square"></div>
      <div class="brand-name">RKW Holdings</div>
    </div>
  </section>

  <section class="card card-back">
    <div class="back-brand">RKW Holdings</div>
    <div class="contact-block">
      <div class="person-name">MARCUS OLVANE</div>
      <div class="person-title">Director</div>
      <div class="title-rule"></div>
      <div class="address">418, 9th Street,<br>Brooklyn NY 11218</div>
      <ul class="contact-list">
        <li><svg viewBox="0 0 10 10"><path d="M2 1 L4 1 L4.6 3 L3.4 4 Q4.5 6 6 6.6 L7 5.4 L9 6 L9 8 Q5 9 1 3 Z"/></svg>(917) 482-0657</li>
        <li><svg viewBox="0 0 10 10"><rect x="1" y="2" width="8" height="6"/><path d="M1 2 L5 5.5 L9 2"/></svg>marcus@rkwholdings-example.com</li>
        <li><svg viewBox="0 0 10 10"><circle cx="5" cy="5" r="4"/><path d="M1 5 H9 M5 1 Q2.5 5 5 9 Q7.5 5 5 1"/></svg>www.<span class="web-accent">rkwholdings-example</span>.com</li>
      </ul>
    </div>
    <div class="back-square"></div>
  </section>
</body>
</html>
```